Buch-/eBook-Cover für einen Elternratgeber
Zielgruppe
Buch: Elternratgeber
Titel: Zahlen fühlen
Untertitel: Deinem Kind den richtigen Umgang beibringen
Wir sind der ULM Verlag und suchen ein passendes Cover für unseren neuen Elternratgeber. Mit diesem Buch möchten wir Eltern unterstützen, ihren Kindern einen guten und verantwortungsvollen Umgang mit Geld zu vermitteln.
Anforderungen an das Cover-Design:
Bitte keinen Comicstil
Das Buch richtet sich an Eltern (nicht kindlich oder verspielt gestalten)
Keine direkte Darstellung von Geld (z. B. keine Münzen, Geldscheine, Sparschweine usw.)
Ob mit oder ohne Personen auf dem Cover: sind wir offen
Farbwahl und Bildsprache: gerne seriös, ansprechend und modern
Wir sind gespannt auf kreative und professionelle Vorschläge!
E-Book E-Book"
Das Design darf nicht zu überladen sein.

```html
<!DOCTYPE html>
<html lang="de">
<head>
<meta charset="utf-8">
<title>Zahlen fühlen – Buchcover</title>
<link rel="stylesheet" href="https://fonts.googleapis.com/css2?family=Bebas+Neue&display=swap">
<style>
  :root {
    --page-bg: #e8e9ee;
    --cover-lilac: #b6b8db;
    --ink-navy: #2a2f66;
    --paper-white: #f4f2ee;
    --note-pink: #d9a6b4;
    --note-cream: #efe6df;
    --note-violet: #a89bc4;
  }
  * { margin: 0; padding: 0; box-sizing: border-box; }
  html, body {
    width: 1200px;
    height: 1200px;
    overflow: hidden;
    background: var(--page-bg);
  }
  .cover {
    position: absolute;
    left: 221px;
    top: 0;
    width: 757px;
    height: 1200px;
    background: var(--cover-lilac);
    font-family: "Bebas Neue", "Arial Narrow", sans-serif;
    color: var(--ink-navy);
  }
  .title {
    position: absolute;
    left: 0;
    width: 100%;
    text-align: center;
    line-height: 1;
  }
  .title-main {
    top: 18px;
    font-size: 220px;
    letter-spacing: 2px;
  }
  .title-sub {
    top: 212px;
    font-size: 136px;
    letter-spacing: 2px;
  }
  .subtitle-band {
    position: absolute;
    left: 49px;
    top: 340px;
    width: 655px;
    height: 143px;
    background: var(--ink-navy);
    color: var(--paper-white);
    display: flex;
    flex-direction: column;
    justify-content: center;
    align-items: center;
    font-size: 60px;
    line-height: 0.98;
    letter-spacing: 0.5px;
    text-align: center;
  }
  .cover-art {
    position: absolute;
    left: 60px;
    top: 540px;
    width: 690px;
    height: 540px;
  }
  .publisher {
    position: absolute;
    left: 298px;
    top: 1126px;
    width: 179px;
    height: 44px;
    background: var(--ink-navy);
    color: var(--paper-white);
    font-size: 36px;
    line-height: 44px;
    text-align: center;
  }
</style>
</head>
<body>
  <main class="cover">
    <h1 class="title title-main">Zahlen</h1>
    <p class="title title-sub">Fühlen</p>

    <div class="subtitle-band">
      <span>Deinem Kind den richtigen</span>
      <span>Umgang beibringen</span>
    </div>

    <svg class="cover-art" viewBox="60 540 690 540" role="img" aria-label="Foto eines zu einem Schmetterling gefalteten Papierobjekts mit dunkler Schattenfläche">
      <defs>
        <linearGradient id="fold-tones" x1="0" y1="0" x2="1" y2="0">
          <stop offset="0" stop-color="var(--note-cream)"/>
          <stop offset="0.45" stop-color="var(--note-violet)"/>
          <stop offset="1" stop-color="var(--note-pink)"/>
        </linearGradient>
      </defs>
      <polygon class="art-shadow" fill="var(--ink-navy)"
        points="736,630 600,1068 145,1068 160,980 620,640"/>
      <polygon class="art-placeholder" fill="url(#fold-tones)"
        points="72,549 366,655 658,552 607,1058 380,1040 366,870 124,1047"/>
    </svg>

    <div class="publisher">ULM Verlag</div>
  </main>
</body>
</html>
```